Buch-/E-Book-Cover für Sammlung von positiven Erfahrungen
Zielgruppe
die Zielgruppe sind Väter die ihren Söhne eine Sammlung von Empfehlungen für ein positives Leben schenken sollen. Der Titel des Buches heisst 'Unter hellen Kiefern'
Aufgabenstellung
ich möchte mich hier von den Designern überraschen und inspirieren lassen.

```html
<!DOCTYPE html>
<html lang="de">
<head>
<meta charset="utf-8">
<title>Unter hellen Kiefern – Buchcover</title>
<link rel="stylesheet" href="https://fonts.googleapis.com/css2?family=League+Spartan:wght@600&display=swap">
<style>
  :root {
    --stage: #e9e9e7;
    --paper: #ffffff;
    --pine: #1f7a4b;
    --pine-light: #23804f;
    --pine-dark: #1b7044;
    --title: #ffffff;
  }
  html, body {
    margin: 0;
    width: 1200px;
    height: 1200px;
    overflow: hidden;
    background: var(--stage);
  }
  .cover {
    position: absolute;
    left: 300px;
    top: 45px;
    width: 600px;
    height: 1110px;
    background: var(--paper);
    box-shadow: 0 2px 10px rgba(0,0,0,0.08);
    overflow: hidden;
  }
  .cover__bands {
    position: absolute;
    inset: 0;
    width: 600px;
    height: 1110px;
  }
  .cover__title {
    position: absolute;
    margin: 0;
    font-family: "League Spartan", sans-serif;
    font-weight: 600;
    font-size: 100px;
    line-height: 110px;
    letter-spacing: 0;
    color: var(--title);
    text-transform: uppercase;
    white-space: nowrap;
  }
  .cover__title--top {
    left: 50px;
    top: 80px;
  }
  .cover__title--bottom {
    right: 50px;
    top: 885px;
    text-align: right;
  }
  .cover__title span { display: block; }
</style>
</head>
<body>
  <main class="cover">
    <svg class="cover__bands" viewBox="0 0 600 1110" aria-hidden="true">
      <path fill="var(--pine)" d="M44 58 L560 54 L574 100 L556 176 L30 178 L40 120 Z"/>
      <path fill="var(--pine)" d="M26 166 L556 170 L572 220 L552 288 L30 290 L18 230 Z"/>
      <path fill="var(--pine-light)" d="M30 278 L566 282 L578 330 L556 400 L44 398 L26 340 Z"/>
      <path fill="var(--pine)" d="M56 392 L574 394 L580 440 L566 512 L52 508 L44 450 Z"/>
      <path fill="var(--pine-light)" d="M18 506 L568 508 L580 560 L560 618 L24 616 L12 560 Z"/>
      <path fill="var(--pine-dark)" d="M44 628 L572 632 L584 680 L564 728 L50 724 L36 676 Z"/>
      <path fill="var(--pine)" d="M38 720 L556 724 L572 780 L548 880 L44 876 L30 800 Z"/>
      <path fill="var(--pine)" d="M30 870 L566 874 L580 930 L566 990 L36 992 L24 930 Z"/>
      <path fill="var(--pine-light)" d="M36 980 L566 984 L576 1010 L552 1040 L42 1036 L28 1008 Z"/>
    </svg>
    <h1 class="cover__title cover__title--top"><span>Unter</span><span>hellen</span></h1>
    <p class="cover__title cover__title--bottom"><span>Kiefern</span></p>
  </main>
</body>
</html>
```